(2) WordPress Website Design & Theme - Velder Auction

Need a WordPress design for a company.

The company is an auction company wanting a responsive, simple and easy to use site. Current site to be upgraded: http://velderauction-example.com/

After a design is chosen, we are going to need our responsive WordPress theme customized to match the design.

We will send you the theme after your design is chosen.

Plug-ins we add, please keep in mind for use in your design:
disable-comments
pagewheel
streamtube clip showcase
lumen fields

Target Market(s)

Industry/Entity Type

It Company

Number of Pages Required

1 page

Font styles to use
Serif
Sans Serif

Requirements
Must have
• Navigation Menu:
• 1. Home - Use current logo in header, include phone number (7219) and email in header along with social media links, also include email sign up in the header. Want to have the list of services on the home page, but to read as follows: Real Estate – Equipment – Minerals – Antiques – Personal Property – Estates – Liquidations – Appraisals. Interested in a static image on the home page, possible a photo slider. Want all 3 auctioneers listed on the home page in this order. Warren, Dustin, Ned. Only need to include the phone number for each. Use the 7219 number for Warren. Their names and phone numbers should be included in the footer. DO NOT use their fax number anywhere on their new site.
• 2. Auction Calendar - is a proprietary plug-in, listing auctions
• 3. About Us.
• 4. Contact Us
• 5. Auction Results
• This website must be responsive. If your design is chosen, you will be expected to customize our responsive theme to match the design.
• Use yellow, black and some brown for colors of the site from the logo.
Nice to have
• Social media buttons, email sign up.

```html
<!DOCTYPE html>
<html lang="en">
<head>
<meta charset="utf-8">
<title>Velder Auction &amp; Reality</title>
<link rel="stylesheet" href="https://fonts.googleapis.com/css2?family=Open+Sans:wght@400;600;700;800&display=swap">
<style>
:root{
  --orange:#f7941d;
  --brown:#6b3f1d;
  --ink:#2b2b2b;
  --text:#666;
  --line:#dcdcdc;
  --band:#ececec;
  --footer:#2f2f2f;
  --footer-deep:#232323;
  --white:#fff;
}
*{box-sizing:border-box;margin:0;padding:0}
html,body{width:736px;height:1200px;overflow:hidden}
body{font-family:"Open Sans",Arial,sans-serif;color:var(--text);background:var(--white);font-size:7px;line-height:1.45}
.canvas{width:736px;height:1200px;position:relative;overflow:hidden}
.btn{display:inline-block;background:var(--orange);color:var(--white);font-weight:600;font-size:7px;padding:5px 12px;border-radius:2px}
h2.section-title{font-size:11px;font-weight:800;color:var(--ink);text-transform:uppercase;margin-bottom:8px}

/* header */
.site-header{height:50px;display:flex;align-items:center;padding:0 22px;justify-content:space-between}
.brand{display:flex;align-items:center;gap:6px}
.brand-mark{width:12px;height:12px;background:var(--orange)}
.brand-name{font-weight:800;font-size:13px;color:var(--brown);line-height:1}
.brand-place{font-size:6px;color:var(--brown);font-weight:800;margin-top:2px}
.signup{display:flex;gap:3px}
.signup .field{width:98px;height:16px;border:1px solid var(--line);font-size:6px;padding:3px 5px;color:#999}
.signup .btn{padding:3px 10px;height:16px}
.header-contacts{display:flex;gap:18px}
.hc{display:flex;align-items:center;gap:5px;font-size:6px;color:var(--ink);white-space:nowrap}
.hc .ic{width:16px;height:16px;border-radius:50%;background:var(--orange);display:flex;align-items:center;justify-content:center;flex:none}

/* nav */
.main-nav{height:30px;border-top:1px solid var(--line);border-bottom:1px solid var(--line);display:flex;align-items:center;padding:0 22px}
.main-nav a{font-size:7px;font-weight:700;color:var(--ink);padding:0 13px;border-right:1px solid var(--line);text-transform:uppercase}
.main-nav a:first-child{padding-left:4px}
.social{margin-left:auto;display:flex;align-items:center;gap:4px;font-size:6.5px;font-weight:600;color:var(--ink)}
.social span.dot{width:12px;height:12px;border-radius:50%;display:inline-block}
.dot.a{background:#3b5a98}.dot.b{background:#4aa8e0}.dot.c{background:#2f77b5}.dot.d{background:#d23a2a}

/* hero */
.hero{margin:16px 60px 0;height:348px;border:4px solid #e5e5e5;position:relative;background:linear-gradient(180deg,#cfe4f3 0%,#b6d1e6 40%,#8fa98a 72%,#5d7f45 100%)}
.hero-copy{position:absolute;left:28px;top:92px}
.hero-copy .names{font-size:16px;font-weight:800;color:var(--ink);line-height:1.2}
.hero-copy .role{font-size:12px;font-weight:600;color:var(--ink);margin:5px 0 12px;line-height:1.3}

/* welcome */
.welcome{text-align:center;padding:12px 80px 0;height:46px}
.welcome h1{font-size:11px;font-weight:800;color:var(--ink);margin-bottom:4px}
.welcome p{font-size:6.5px;line-height:1.4}

/* three columns */
.info-row{display:flex;gap:16px;padding:10px 28px 0;height:210px}
.services{width:122px}
.services li{list-style:none;border:1px solid var(--line);border-bottom:none;padding:4px 8px;font-size:6.5px;color:var(--ink)}
.services li:last-child{border-bottom:1px solid var(--line)}
.news{width:190px}
.news-item{display:flex;gap:6px;margin-bottom:6px}
.thumb{flex:none}
.news-item h3{font-size:6.5px;font-weight:700;color:var(--ink)}
.news-item .date{font-size:6px;color:#999}
.news p{margin-bottom:8px}
.contact{flex:1}
.contact .lines{display:flex;gap:18px;margin:6px 0 8px;color:var(--ink)}
.form{display:flex;gap:6px}
.form .col{display:flex;flex-direction:column;gap:5px;width:100px}
.input{height:15px;border:1px solid var(--line);font-size:6px;padding:3px 5px;color:#999}
.textarea{flex:1;height:55px;border:1px solid var(--line);font-size:6px;padding:3px 5px;color:#999}
.form-actions{text-align:right;margin-top:5px}

/* recent */
.recent{display:flex;gap:14px;padding:0 28px;height:162px}
.recent-intro{width:118px}
.recent-intro p{margin-bottom:8px}
.card{width:172px}
.card h3{font-size:6.5px;font-weight:700;color:var(--ink);margin:6px 0 2px}
.more{color:var(--ink);font-weight:600;font-size:6.5px}
.more b{color:var(--orange)}

/* auctioneers */
.auctioneers{background:var(--band);height:82px;padding:8px 28px 0}
.auctioneers .head{font-size:7px;font-weight:700;color:var(--ink);margin-bottom:6px}
.auctioneers .head strong{font-size:11px;color:var(--ink);font-weight:800;margin-right:6px}
.team{display:flex;gap:40px;padding-left:10px}
.person{display:flex;gap:8px;width:190px}
.person h4{font-size:7px;font-weight:800;color:var(--ink)}
.person .phone{color:var(--orange);font-weight:700}

/* footer */
.site-footer{background:var(--footer);height:236px;padding:22px 28px 0;display:flex;gap:24px;color:#aaa}
.f-col{flex:1}
.f-col h5{font-size:8px;font-weight:700;color:var(--white);margin-bottom:8px;text-transform:uppercase}
.f-col li{list-style:none;font-size:6.5px;margin-bottom:4px}
.f-col .split{display:flex;gap:14px}
.f-col .more{color:var(--white)}
.c-line{display:flex;gap:5px;align-items:center;margin-bottom:6px;font-size:6.5px}
.footer-bar{background:var(--footer-deep);height:20px;padding:0 28px;display:flex;align-items:center;justify-content:space-between;color:#999;font-size:6.5px}
.footer-bar .social{color:#bbb;margin-left:0}
.footer-bar .social span.dot{width:9px;height:9px}
</style>
</head>
<body>
<div class="canvas">

  <header class="site-header">
    <div class="brand">
      <span class="brand-mark"></span>
      <div>
        <div class="brand-name">VELDER AUCTION &amp; REALITY</div>
        <div class="brand-place">ASHVALE, OK</div>
      </div>
    </div>
    <form class="signup">
      <div class="field">Enter your email</div>
      <span class="btn">Subscribe</span>
    </form>
    <div class="header-contacts">
      <div class="hc">
        <span class="ic"><svg width="8" height="8" viewBox="0 0 10 10"><path d="M2 1l2 2-1 1.5c.6 1.2 1.4 2 2.5 2.5L7 6l2 2-1.5 1.5C4.5 9 1 5.5.5 2.5z" fill="#fff"/></svg></span>
        <div>Call us<br><strong>(555) 010-7219</strong></div>
      </div>
      <div class="hc">
        <span class="ic"><svg width="9" height="7" viewBox="0 0 10 8"><rect x=".5" y=".5" width="9" height="7" fill="none" stroke="#fff"/><path d="M.5 .5l4.5 4 4.5-4" fill="none" stroke="#fff"/></svg></span>
        <div>Email us<br>velderauction@example.com</div>
      </div>
    </div>
  </header>

  <nav class="main-nav">
    <a>Home</a><a>Auctions</a><a>Results</a><a>About Us</a><a>Contact Us</a>
    <div class="social">Connect with our social network <span class="dot a"></span><span class="dot b"></span><span class="dot c"></span><span class="dot d"></span></div>
  </nav>

  <section class="hero" role="img" aria-label="Photo of modern high-rise buildings among green trees under a pale sky">
    <div class="hero-copy">
      <div class="names">WARREN, NED,<br>DUSTIN VELDER</div>
      <div class="role">LICENSED REAL ESTATE BROKERS AND<br>AUCTIONEERS</div>
      <span class="btn">Read our History</span>
    </div>
  </section>

  <section class="welcome">
    <h1>WELCOME TO VELDER AUCTION &amp; REALITY</h1>
    <p>There are many ways to sell property, and an open public auction brings buyers together in one place at one time. Our family team has handled estates, land and equipment sales across the region for many years and is glad to help you with yours.</p>
  </section>

  <section class="info-row">
    <ul class="services">
      <li>Real Estate</li><li>Equipment</li><li>Minerals</li><li>Antiques</li><li>Personal Property</li><li>Estates</li><li>Liquidations</li><li>Appraisals</li>
    </ul>
    <div class="news">
      <h2 class="section-title">Latest News</h2>
      <div class="news-item">
        <div class="thumb" role="img" aria-label="News photo of a city street" style="width:58px;height:44px;background:linear-gradient(160deg,#9fb6c8,#6f7f70)"></div>
        <div>
          <h3>LOREM IPSUM IS SIMPLY DUMMY TEXT OF THE PRINTING</h3>
          <div class="date">Posted by | 12 April 2015</div>
        </div>
      </div>
      <p>Lorem ipsum is simply dummy text of the printing and typesetting industry. Lorem ipsum has been the industry standard dummy text ever since the 1500s, when an unknown printer.</p>
      <span class="btn">Read more</span>
    </div>
    <div class="contact">
      <h2 class="section-title">Contact Us</h2>
      <p>Lorem ipsum is simply dummy text of the printing and typesetting industry.</p>
      <div class="lines"><span><strong>(555) 010-7219</strong></span><span>velderauction@example.com</span></div>
      <div class="form">
        <div class="col"><div class="input">Name</div><div class="input">Email</div><div class="input">Phone</div></div>
        <div class="textarea">Message</div>
      </div>
      <div class="form-actions"><span class="btn">Submit</span></div>
    </div>
  </section>

  <section class="recent">
    <div class="recent-intro">
      <h2 class="section-title">Recent Actions</h2>
      <p>Lorem ipsum is simply dummy text of the printing and typesetting industry. Lorem ipsum has been the industry standard dummy text ever since the 1500s, when an unknown printer.</p>
      <span class="btn">Read more</span>
    </div>
    <article class="card">
      <div role="img" aria-label="Photo of green farmland with a row of trees" style="height:82px;background:linear-gradient(180deg,#b9cfe0,#6f9a4a)"></div>
      <h3>LOREM IPSUM IS SIMPLY DUMMY TEXT OF THE PRINTING...</h3>
      <span class="more"><b>›</b> View details</span>
    </article>
    <article class="card">
      <div role="img" aria-label="Aerial photo of a town and open land" style="height:82px;background:linear-gradient(180deg,#c7d3dc,#8b8f73)"></div>
      <h3>LOREM IPSUM IS SIMPLY DUMMY TEXT OF THE PRINTING...</h3>
      <span class="more"><b>›</b> View details</span>
    </article>
    <article class="card">
      <div role="img" aria-label="Photo of a road through green fields" style="height:82px;background:linear-gradient(180deg,#d6e1ea,#4f8a3a)"></div>
      <h3>LOREM IPSUM IS SIMPLY DUMMY TEXT OF THE PRINTING...</h3>
      <span class="more"><b>›</b> View details</span>
    </article>
  </section>

  <section class="auctioneers">
    <div class="head"><strong>AUCTIONEERS</strong>WARREN, NED, DUSTIN VELDER LICENSED REAL ESTATE BROKERS AND AUCTIONEERS</div>
    <div class="team">
      <div class="person">
        <div class="thumb" role="img" aria-label="Portrait photo of Warren" style="width:44px;height:44px;background:linear-gradient(180deg,#b8a08a,#6d5a4a)"></div>
        <div><h4>WARREN</h4><p>Lorem ipsum is simply dummy text of the printing and typesetting.</p><span class="phone">(555) 010-7219</span></div>
      </div>
      <div class="person">
        <div class="thumb" role="img" aria-label="Portrait photo of Dustin" style="width:44px;height:44px;background:linear-gradient(180deg,#b8a08a,#6d5a4a)"></div>
        <div><h4>DUSTIN</h4><p>Lorem ipsum is simply dummy text of the printing and typesetting.</p><span class="more"><b>›</b> View details</span></div>
      </div>
      <div class="person">
        <div class="thumb" role="img" aria-label="Portrait photo of Ned" style="width:44px;height:44px;background:linear-gradient(180deg,#b8a08a,#6d5a4a)"></div>
        <div><h4>NED</h4><p>Lorem ipsum is simply dummy text of the printing and typesetting.</p><span class="more"><b>›</b> View details</span></div>
      </div>
    </div>
  </section>

  <footer class="site-footer">
    <div class="f-col">
      <h5>Who we are</h5>
      <p>Lorem ipsum is simply dummy text of the printing and typesetting industry. Lorem ipsum has been the industry standard dummy text ever since the 1500s, when an unknown printer took a galley.</p>
      <p style="margin-top:8px"><span class="more">Read more →</span></p>
    </div>
    <div class="f-col">
      <h5>Welcome</h5>
      <ul><li>Home</li><li>Auctions</li><li>Results</li><li>About us</li><li>Contact us</li></ul>
    </div>
    <div class="f-col">
      <h5>Services</h5>
      <div class="split">
        <ul><li>Real Estate</li><li>Equipment</li><li>Minerals</li><li>Antiques</li></ul>
        <ul><li>Personal Property</li><li>Estates</li><li>Liquidations</li><li>Appraisals</li></ul>
      </div>
    </div>
    <div class="f-col">
      <h5>Contact Info</h5>
      <div class="c-line">Ashvale, OK</div>
      <div class="c-line">Warren (555) 010-7219</div>
      <div class="c-line">velderauction@example.com</div>
    </div>
  </footer>
  <div class="footer-bar">
    <span>© 2015 Velder Auction. All rights reserved</span>
    <div class="social">Connect with our social network <span class="dot a"></span><span class="dot b"></span><span class="dot c"></span><span class="dot d"></span></div>
  </div>

</div>
</body>
</html>
```